Business Card Design Project

Design business card based on logo provided.

Industry/Entity Type

Business

Requirements
Nice to have
• Logo to be provided.

Solid green second side with reverse logo (buildings only, not text).

Because the logo is linear I think that it might be possible to extend the logo lines across the card (only on the second side) as an interesting design element.

"Guiding Clients Toward Stronger Project Delivery"

"Job Order Contracting and Best Value Specialist"

"Cooperation - Innovation - Efficiency"

Basic Info:
Dana Marwick
Owner/Founder
505-817-6052
dana@danamarwickpartners.example

www.danamarwickpartners.example (this should probably be on reverse)

```html
<!DOCTYPE html>
<html lang="en">
<head>
<meta charset="utf-8">
<title>Dana Marwick Partners — Business Cards</title>
<link rel="stylesheet" href="https://fonts.googleapis.com/css2?family=Oswald:wght@500&family=Arimo:wght@400;700&display=swap">
<style>
  :root {
    --stage: #3a3a3a;
    --green-light: #a6c33b;
    --green-dark: #6e9133;
    --green-band: #7f9c35;
    --green-text: #97b83a;
    --ink: #2b2b2b;
    --paper: #ffffff;
  }
  * { box-sizing: border-box; margin: 0; padding: 0; }
  html, body { width: 1200px; height: 534px; overflow: hidden; }
  body {
    background: var(--stage);
    position: relative;
    font-family: "Arimo", Arial, sans-serif;
  }
  .card {
    position: absolute;
    top: 119px;
    width: 517px;
    height: 295px;
    overflow: hidden;
  }
  .card--front {
    left: 62px;
    background: linear-gradient(180deg, var(--green-light) 0%, var(--green-dark) 100%);
    color: var(--paper);
  }
  .card--back { left: 619px; background: var(--paper); color: var(--ink); }

  .brand {
    display: flex;
    align-items: center;
    gap: 10px;
    font-family: "Oswald", "Arial Narrow", sans-serif;
    font-weight: 500;
    text-transform: uppercase;
    letter-spacing: 0.5px;
    white-space: nowrap;
  }
  .brand__mark { display: block; flex: none; }

  .card--front .brand {
    position: absolute;
    right: 22px;
    top: 182px;
    font-size: 34px;
    color: var(--paper);
  }
  .card--front .brand__mark { width: 22px; height: 22px; background: var(--paper); }
  .front__web {
    position: absolute;
    right: 24px;
    top: 254px;
    font-size: 12.5px;
  }

  .card--back .brand {
    position: absolute;
    left: 30px;
    top: 70px;
    gap: 28px;
    font-size: 21px;
    color: var(--green-dark);
  }
  .card--back .brand__mark { width: 34px; height: 34px; background: var(--green-dark); }

  .person { position: absolute; left: 28px; top: 150px; }
  .person__name { font-size: 20px; font-weight: 700; color: var(--green-text); }
  .person__role { font-size: 12.5px; margin-top: 2px; }

  .contact {
    position: absolute;
    left: 182px;
    top: 152px;
    list-style: none;
    font-size: 12.5px;
    line-height: 16.5px;
  }
  .contact__label { color: var(--green-text); margin-right: 3px; }

  .tagline-band {
    position: absolute;
    left: 0; right: 0;
    top: 233px;
    height: 40px;
    background: var(--green-band);
    color: var(--paper);
    font-weight: 700;
    font-size: 13px;
    display: flex;
    align-items: center;
    justify-content: center;
  }
</style>
</head>
<body>
  <section class="card card--front" aria-label="Card front">
    <div class="brand"><span class="brand__mark"></span><span class="brand__name">Dana Marwick Partners</span></div>
    <p class="front__web">www.danamarwickpartners.example</p>
  </section>

  <section class="card card--back" aria-label="Card back">
    <div class="brand"><span class="brand__mark"></span><span class="brand__name">Dana Marwick Partners</span></div>
    <div class="person">
      <p class="person__name">Dana Marwick</p>
      <p class="person__role">Owner/Founder</p>
    </div>
    <ul class="contact">
      <li><span class="contact__label">p:</span>505-817-6052</li>
      <li><span class="contact__label">e:</span>dana@danamarwickpartners.example</li>
      <li><span class="contact__label">w:</span>www.danamarwickpartners.example</li>
    </ul>
    <div class="tagline-band">Guiding Clients Toward Stronger Project Delivery</div>
  </section>
</body>
</html>
```